Tovrell Family Reunion Flyer

A flyer detailing family reunion events. It should be complimentary to the logo style and fonts. BE DIFFERENT AVOID TEMPLATES

The 2015 Tovrell Family Reunion
Descendants of Besoda Nwaruk Felim Tovrell

Friday August 14th 2pm
Jummah Prayer At Suravan Mosque
Followed by Family Get Together

Saturday august 15th 12pm
Family Reunion Picnic
4127 tovrell Dr.
bowie

Hosted by the Children of The Prestigious Tovrell Family

Industry/Entity Type

Events

Colors
0355a3
9bcb3c

Requirements
Must have
• Logo

```html
<!DOCTYPE html>
<html lang="en">
<head>
<meta charset="utf-8">
<title>The 2015 Tovrell Family Reunion</title>
<link href="https://fonts.googleapis.com/css2?family=Anton&family=Pathway+Gothic+One&family=Oswald:wght@500;700&display=swap" rel="stylesheet">
<style>
  :root {
    --reunion-blue: #0355a3;
    --reunion-green: #9bcb3c;
    --accent-red: #e8262b;
    --white: #ffffff;
    --tree-dark: #3b3a33;
    --tree-mid: #8c8a7c;
    --sky-light: #e9ecef;
  }
  * { margin: 0; padding: 0; box-sizing: border-box; }
  html, body { width: 861px; height: 1200px; overflow: hidden; background: #ffffff; }
  .flyer {
    position: relative;
    width: 861px;
    height: 1200px;
    overflow: hidden;
    background: var(--reunion-blue);
  }

  /* Header band */
  .header {
    position: absolute; left: 0; top: 0;
    width: 861px; height: 238px;
    background: var(--reunion-green);
  }
  .title {
    position: absolute; left: 40px; top: 28px;
    font-family: "Anton", "Oswald", sans-serif;
    color: var(--reunion-blue);
    line-height: 0.95;
    text-transform: uppercase;
  }
  .title-year { display: block; font-size: 56px; letter-spacing: 1px; }
  .title-name { display: block; font-size: 76px; letter-spacing: 1px; }
  .title-event { display: block; font-size: 44px; letter-spacing: 0.5px; }

  .brand {
    position: absolute; left: 600px; top: 22px;
    width: 220px; text-align: center;
  }
  .brand-mark {
    display: block; margin: 0 auto;
    width: 172px; height: 172px;
    border-radius: 50%;
    background: var(--reunion-blue);
  }
  .brand-name {
    display: block; margin-top: 10px;
    font-family: "Oswald", sans-serif; font-weight: 500;
    font-size: 17px; color: var(--reunion-blue);
    white-space: nowrap;
  }

  /* Lineage heading */
  .lineage {
    position: absolute; left: 0; top: 262px;
    width: 861px; text-align: center;
    font-family: "Anton", "Oswald", sans-serif;
    color: var(--white); text-transform: uppercase;
    line-height: 1.05;
  }
  .lineage-intro { display: block; font-size: 40px; letter-spacing: 1px; }
  .lineage-ancestor { display: block; font-size: 36px; letter-spacing: 1px; }
  .lineage-name { display: block; font-size: 78px; letter-spacing: 2px; margin-top: 4px; }

  /* Tree photo area */
  .tree-photo {
    position: absolute; left: 0; top: 468px;
    width: 861px; height: 510px;
    background: linear-gradient(100deg, var(--tree-dark) 0%, #5a584d 30%, var(--tree-mid) 55%, #b9bab3 78%, var(--sky-light) 100%);
  }
  .tree-shade {
    position: absolute; left: 0; top: 468px;
    width: 861px; height: 510px;
    background: linear-gradient(180deg, rgba(0,0,0,0.35) 0%, rgba(0,0,0,0) 40%, rgba(0,0,0,0.25) 100%);
  }

  .events {
    position: absolute; left: 420px; top: 520px;
    width: 420px;
    font-family: "Pathway Gothic One", "Oswald", sans-serif;
    color: var(--white);
    text-align: center;
  }
  .event { margin-bottom: 46px; }
  .event-when { display: block; color: var(--accent-red); font-size: 38px; line-height: 1.1; }
  .event-detail { display: block; font-size: 34px; line-height: 1.12; text-shadow: 0 1px 3px rgba(0,0,0,0.45); }

  /* Footer */
  .flowers {
    position: absolute; left: 0; top: 978px;
    width: 420px; height: 222px;
    background: radial-gradient(circle at 30% 55%, #f08bb5 0%, #c8d55a 35%, #2c7fc2 75%, var(--reunion-blue) 100%);
  }
  .host {
    position: absolute; left: 450px; top: 1004px;
    width: 390px; text-align: right;
    font-family: "Oswald", sans-serif; font-weight: 700;
    text-transform: uppercase; line-height: 1.1;
  }
  .host-label {
    display: block; font-family: "Pathway Gothic One", sans-serif; font-weight: 400;
    text-transform: none; color: var(--white); font-size: 40px; margin-bottom: 4px;
  }
  .host-line { display: block; color: var(--accent-red); font-size: 30px; }
  .host-family { display: block; color: var(--accent-red); font-size: 46px; }
</style>
</head>
<body>
<main class="flyer">
  <header class="header">
    <h1 class="title">
      <span class="title-year">The 2015</span>
      <span class="title-name">Tovrell</span>
      <span class="title-event">Family Reunion</span>
    </h1>
    <div class="brand">
      <span class="brand-mark" aria-hidden="true"></span>
      <span class="brand-name">Tovrell Family Reunion 2015</span>
    </div>
  </header>

  <h2 class="lineage">
    <span class="lineage-intro">Descendants of</span>
    <span class="lineage-ancestor">Besoda Nwaruk</span>
    <span class="lineage-name">Felim Tovrell</span>
  </h2>

  <div class="tree-photo" role="img" aria-label="Photograph of a large spreading tree with dark branches against a pale sky"></div>
  <div class="tree-shade" aria-hidden="true"></div>

  <section class="events">
    <div class="event">
      <span class="event-when">Friday August 14th 2pm</span>
      <span class="event-detail">Jummah Prayer At Suravan Mosque</span>
      <span class="event-detail">Followed by Family Get Together</span>
    </div>
    <div class="event">
      <span class="event-when">Saturday August 15th 12pm</span>
      <span class="event-detail">Family Reunion Picnic</span>
      <span class="event-detail">4127 Tovrell Dr.</span>
      <span class="event-detail">Bowie</span>
    </div>
  </section>

  <div class="flowers" role="img" aria-label="Colourful illustrated flowers and leaves in pink, yellow-green and blue"></div>

  <footer class="host">
    <span class="host-label">Hosted by</span>
    <span class="host-line">The Children of</span>
    <span class="host-line">The Prestigious</span>
    <span class="host-family">Tovrell Family</span>
  </footer>
</main>
</body>
</html>
```